Design a Website Mockup for CounselBidHub.com

[url removed, login to view] is a website we are building where Clients can post a brief summary of their case and Attorneys can bid on the job--this way the client gets the best Attorney for the least amount of money. This site will be basically a combination of a site like this one and Lawful Nest. We bought a script and it is uploaded at CounselBidHub.com. The script is basically just a framework that we are working from. Please find the powerpoint presentation attached that is just a framework to work form for each of the pages listed in the presentation. The logo will be bigger than it currently appears on the site. But please incorporate the logo where you feel it should be. The current colors of the site are off. But we would like the colors to be similar to those that are in the logo. Basically we're going for a clean, classic American attorney look and feel for the site. The design colors should be brown, green and gold. But where our clients need to input text should be mostly white like this page.

PLEASE NOTE: We just uploaded "A rough draft of the homepage" this is a compilation of all of the elements that we have liked from your submissions. If you see one of your elements in our final draft you will be compensated a fair amount for that element if you're not the winner.

*A winner is Guaranteed
*If we see pages that we like from other applicants we will compensate you if we decide to use any of your pages on a single basis.

```html
<!DOCTYPE html>
<html lang="en">
<head>
<meta charset="utf-8">
<title>CounselBidHub.com – Home</title>
<link href="https://fonts.googleapis.com/css2?family=Cinzel:wght@400;700&family=Mulish:wght@400&display=swap" rel="stylesheet">
<style>
  :root {
    --cream: #fdf7e9;
    --map-tone: #f6e6c6;
    --brown-dark: #4a220c;
    --brown-mid: #7a4019;
    --brown-nav: #a77a4b;
    --brown-nav-low: #8b5b2f;
    --brown-active: #5a2c10;
    --ink: #2b1608;
    --body-text: #3a3128;
    --button-text: #fbecd3;
    --copyright: #8a5a30;
  }
  * { margin: 0; padding: 0; box-sizing: border-box; }
  html, body { width: 1200px; height: 833px; overflow: hidden; }
  body {
    position: relative;
    background: var(--cream);
    font-family: "Mulish", "Helvetica Neue", Arial, sans-serif;
    color: var(--body-text);
  }
  .world-map {
    position: absolute; left: 0; top: 0; width: 1200px; height: 470px;
    background: radial-gradient(ellipse 620px 260px at 50% 40%, var(--map-tone), rgba(246,230,198,0.35) 70%, rgba(253,247,233,0) 100%);
  }
  .brand {
    position: absolute; left: 0; top: 80px; width: 1200px; height: 216px;
    display: flex; align-items: center; justify-content: center;
  }
  .brand-name {
    font-family: "Cinzel", Georgia, serif;
    font-weight: 700; font-size: 42px; line-height: 1;
    color: var(--brown-dark);
    white-space: nowrap;
  }
  .role-button {
    position: absolute; top: 331px; width: 264px; height: 56px;
    border-radius: 28px;
    background: linear-gradient(var(--brown-mid), var(--brown-dark));
    box-shadow: 0 0 0 3px #fff, 0 2px 6px rgba(60,30,10,0.35);
    display: flex; align-items: center;
    text-decoration: none;
  }
  .role-button.attorney { left: 313px; }
  .role-button.hire { left: 623px; }
  .role-icon {
    width: 48px; height: 48px; margin-left: 4px;
    border-radius: 50%; background: #fff;
    border: 2px solid #e9dccb; flex: none;
  }
  .role-label {
    flex: 1; text-align: center; padding-right: 8px;
    font-family: "Cinzel", Georgia, serif;
    font-size: 20px; color: var(--button-text);
    white-space: nowrap;
  }
  .welcome-title {
    position: absolute; left: 0; top: 487px; width: 1200px;
    text-align: center;
    font-family: "Cinzel", Georgia, serif; font-weight: 700;
    font-size: 29px; color: var(--ink); letter-spacing: 1px;
  }
  .welcome-text {
    position: absolute; left: 201px; top: 531px; width: 797px;
    font-size: 14.6px; line-height: 24px; text-align: justify;
  }
  .main-nav {
    position: absolute; left: 201px; top: 661px; width: 798px; height: 34px;
    display: flex; border-radius: 3px; overflow: hidden;
    box-shadow: 0 1px 3px rgba(60,30,10,0.4);
  }
  .main-nav a {
    display: flex; align-items: center; justify-content: center;
    color: #fff; font-size: 13.5px; text-decoration: none;
    background: linear-gradient(var(--brown-nav), var(--brown-nav-low));
    border-right: 1px solid rgba(255,255,255,0.25);
  }
  .main-nav a:last-child { border-right: none; }
  .main-nav a.active { background: linear-gradient(#7a4420, var(--brown-active)); }
  .copyright {
    position: absolute; left: 0; top: 740px; width: 1200px;
    text-align: center; font-size: 11.5px; color: var(--copyright);
  }
</style>
</head>
<body>
  <div class="world-map" role="img" aria-label="Faint world map in soft beige across the page header"></div>

  <header class="brand">
    <div class="brand-name">CounselBidHub.com</div>
  </header>

  <a class="role-button attorney" href="#">
    <span class="role-icon" role="img" aria-label="Attorney icon"></span>
    <span class="role-label">I'm an Attorney</span>
  </a>
  <a class="role-button hire" href="#">
    <span class="role-icon" role="img" aria-label="Client at a screen icon"></span>
    <span class="role-label">Hire an Attorney</span>
  </a>

  <h1 class="welcome-title">Welcome to CounselBidHub</h1>
  <p class="welcome-text">CounselBidHub.com is the premier destination for clients to hire the best attorneys at the best rate. CounselBidHub helps Attorneys to grow their business, hire staff, find like-minded attorneys for partnership, shop for office products, get legal news and updates, and much more. Clients can find legal forms and form legal entities, trademark, and file other legal matters directly on our site.</p>

  <nav class="main-nav">
    <a class="active" href="#" style="width:96px">Home</a>
    <a href="#" style="width:151px">Find Attorney</a>
    <a href="#" style="width:119px">Post Case</a>
    <a href="#" style="width:128px">Market Place</a>
    <a href="#" style="width:123px">Law Firms</a>
    <a href="#" style="width:77px">Jobs</a>
    <a href="#" style="width:104px">News</a>
  </nav>

  <footer class="copyright">Copyright 2013 CounselBidHub.com. All Right Reserved.</footer>
</body>
</html>
```